Basic Letterhead Design

We need a Letterhead design. Our company is in the financial services industry. We are a small bank who lends money. I have uploaded an example our current letterhead design. We would like a new one.

```html
<!DOCTYPE html>
<html lang="en">
<head>
<meta charset="utf-8">
<title>Harlow Lending – Letterhead</title>
<link rel="stylesheet" href="https://fonts.googleapis.com/css2?family=Karla:wght@400;500&family=Arimo:wght@400&display=swap">
<style>
  :root {
    --backdrop: #e8e8e8;
    --paper: #f3f3f2;
    --band: #2a2d2a;
    --brand-green: #1f4a33;
    --ink: #3a3a3a;
    --heading-ink: #444444;
    --signature-tone: #d9dcdb;
  }
  * { box-sizing: border-box; margin: 0; padding: 0; }
  html, body {
    width: 1176px; height: 1200px; overflow: hidden;
    background: var(--backdrop);
  }
  .letterhead {
    position: absolute; left: 198px; top: 48px;
    width: 780px; height: 1104px;
    background: var(--paper);
    box-shadow: 0 2px 8px rgba(0,0,0,0.12);
    overflow: hidden;
    font-family: "Arimo", Arial, sans-serif;
    color: var(--ink);
  }
  .edge-band {
    position: absolute; left: 0; top: 0; bottom: 0; width: 14px;
    background: var(--band);
  }
  .edge-tab {
    position: absolute; left: 0; top: 880px;
    width: 44px; height: 88px;
    background: var(--brand-green);
    border: 3px solid #ffffff; border-left: none;
    border-radius: 0 44px 44px 0;
  }
  .brand {
    position: absolute; right: 70px; top: 118px;
    display: flex; align-items: center; gap: 10px;
    font-family: "Karla", Arial, sans-serif;
    font-weight: 500; font-size: 22px; letter-spacing: 1.5px;
    text-transform: uppercase;
    color: var(--brand-green);
  }
  .brand-dot {
    width: 18px; height: 18px; border-radius: 50%;
    background: var(--brand-green);
  }
  .salutation {
    position: absolute; left: 96px; top: 196px;
    font-size: 21px; color: var(--heading-ink);
  }
  .letter-body {
    position: absolute; left: 96px; top: 250px; width: 610px;
    font-size: 11.5px; line-height: 1.55;
  }
  .letter-body p { margin-bottom: 11px; }
  .closing {
    position: absolute; left: 96px; top: 740px;
    font-size: 11.5px;
  }
  .signature {
    position: absolute; left: 96px; top: 770px;
    width: 120px; height: 44px;
    background: var(--signature-tone);
    border-radius: 4px;
  }
  .company-address {
    position: absolute; left: 96px; top: 880px;
    font-family: "Karla", Arial, sans-serif;
    font-size: 17px; line-height: 1.3; letter-spacing: 0.8px;
    color: var(--brand-green);
  }
</style>
</head>
<body>
  <main class="letterhead">
    <div class="edge-band"></div>
    <div class="edge-tab"></div>

    <header class="brand">
      <span class="brand-dot"></span>
      <span class="brand-name">Harlow Lending</span>
    </header>

    <h1 class="salutation">Dear Mr. Carter,</h1>

    <section class="letter-body">
      <p>Lorem ipsum dolor sit amet, consectetur adipiscing elit. Donec orci purus, luctus vitae dignissim eu, iaculis sed purus. Vivamus faucibus, ipsum nec aliquet viverra, leo mauris condimentum ligula, sit amet sagittis enim ligula quis arcu. Nam egestas tortor id nisi porttitor mattis. In tortor ante, ultricies in suscipit a, tempus non massa. Vivamus et auctor mi. Fusce vel massa nulla. Phasellus nec eros mauris, et scelerisque orci.</p>
      <p>Donec malesuada orci vitae nulla accumsan porta a id massa. Quisque accumsan iaculis magna sit amet fringilla. Maecenas consequat, magna eget tincidunt semper, odio nibh rutrum mi, id feugiat ante nisi eu risus. Vestibulum nunc orci, rhoncus a placerat in, ultricies in mi. Cras mattis varius eros, vel fringilla nisi suscipit eget. Quisque scelerisque sagittis nulla at porttitor.</p>
      <p>Sed id augue vitae urna euismod commodo aliquet a quam. Pellentesque arcu velit, cursus et malesuada ut, consequat et diam. Nullam erat sem, rhoncus id ullamcorper vitae, rhoncus et arcu. In ultricies ultricies nulla, ut rutrum nisi iaculis at. Donec eu magna a metus ornare faucibus. Fusce aliquet faucibus ultricies. Morbi semper, est id tincidunt gravida, sem arcu adipiscing lacus, ac bibendum nulla leo eu purus. Quisque nec diam sed risus consectetur accumsan quis quis nibh. Vestibulum id purus lorem.</p>
      <p>It is a long established fact that a reader will be distracted by the readable content of a page when looking at its layout. The point of using Lorem Ipsum is that it has a more-or-less normal distribution of letters, as opposed to using 'Content here, content here', making it look like readable English. Many desktop publishing packages</p>
      <p>ada ut, consequat et diam. Nullam erat sem, rhoncus id ullamcorper vitae, rhoncus et arcu. In ultricies ultricies nulla, ut rutrum nisi iaculis at. Donec eu magna a metus ornare faucibus. Fusce aliquet faucibus ultricies. Morbi semper,</p>
    </section>

    <p class="closing">Sincerely,</p>
    <div class="signature" role="img" aria-label="Handwritten signature of the sender"></div>

    <address class="company-address" style="font-style:normal">
      Harlow Lending Pty Ltd<br>
      47 Banksia Street<br>
      Gymea Nsw 2227<br>
      ACN: 512 880 317
    </address>
  </main>
</body>
</html>
```